Card for modern wood artisan that builds log homes and timber frames.

Design a card with catchy imagery. With a quick list of things I build and services I offer.

I'd like an English side and a french side. I can provide the text.

I am basically a guy that builds log homes and timber frames , but I am very eco friendly oriented.

I use only eco friendly products to limit my carbon footprint.
I want the client to feel as if they are hiring a good smart builder.

I have been building for a while but just starting out to market myself out there , not just work for other companies. Starting
My own thing legitimately.

I am very conscientious, and I take care of the work I do. I am trying to bring a new age, modern feel to an old profession.

Reason: I am not completely satisfied with A model yet, looking for that masculin rustic artistic design that I havent completely found yet. Thank you for your sumbissions.

Target Market(s)

People looking to hire a builder to design and build their projects.
And contractors that want to hire a quality subcontractor for their jobs.

Industry/Entity Type

Construction

Contact Information for Business Card

I want my logo on it, that I had designed here.
And a list of services I provide.

With my phone number, website adress and Email.

Requirements
Must have
• Artful presentation,
• Eco friendly feel
• I love trees.

```html
<!DOCTYPE html>
<html lang="en">
<head>
<meta charset="utf-8">
<title>Norvane Wood Artisan – Business Card</title>
<link rel="stylesheet" href="https://fonts.googleapis.com/css2?family=Oswald:wght@500;600&family=Dosis:wght@400;500;600&display=swap">
<style>
  :root {
    --backdrop: #e7e3dc;
    --card-frame: #b9b0a6;
    --card-paper: #f5f3ee;
    --ink: #1e1c1a;
    --tree-gold: #d99a2b;
    --tree-amber: #c7841c;
    --rule: #2a2724;
  }
  * { box-sizing: border-box; margin: 0; padding: 0; }
  html, body {
    width: 1200px; height: 857px; overflow: hidden;
    background: var(--backdrop);
  }
  .stage {
    width: 1200px; height: 857px;
    display: flex; align-items: center; justify-content: center;
  }
  .card {
    width: 420px; height: 660px;
    background: var(--card-frame);
    padding: 14px;
    display: flex; flex-direction: column;
  }
  .card-face {
    flex: 1;
    background: var(--card-paper);
    position: relative;
    display: flex; align-items: center; justify-content: center;
  }
  .tree-art {
    position: absolute;
    left: 50%; top: 36px;
    width: 210px; height: 360px;
    transform: translateX(-50%);
  }
  .brand {
    position: relative;
    display: flex; flex-direction: column; align-items: center;
    margin-top: 10px;
  }
  .brand-line { display: flex; align-items: center; gap: 12px; }
  .brand-square {
    width: 34px; height: 34px;
    background: var(--ink);
  }
  .brand-name {
    font-family: "Oswald", sans-serif;
    font-weight: 600;
    font-size: 46px;
    letter-spacing: 3px;
    color: var(--ink);
    line-height: 1;
  }
  .brand-tagline {
    font-family: "Oswald", sans-serif;
    font-weight: 500;
    font-size: 15px;
    letter-spacing: 2px;
    color: var(--ink);
    margin-top: 6px;
  }
  .contact-panel {
    height: 212px;
    background: var(--card-frame);
    padding: 12px 0 6px;
    display: grid;
    grid-template-columns: 1.35fr 1fr;
    grid-template-rows: 56px 1fr;
    border-top: 1.5px solid var(--rule);
    color: var(--ink);
    font-family: "Dosis", sans-serif;
  }
  .contact-name {
    grid-column: 1; grid-row: 1;
    font-family: "Oswald", sans-serif;
    font-weight: 600; font-size: 23px; letter-spacing: 1px;
    border-right: 1.5px solid var(--rule);
    border-bottom: 1.5px solid var(--rule);
    padding: 4px 14px;
  }
  .contact-lines {
    grid-column: 1; grid-row: 2;
    border-right: 1.5px solid var(--rule);
    display: flex; flex-direction: column;
  }
  .contact-lines li {
    list-style: none;
    font-size: 13px; font-weight: 500; letter-spacing: .5px;
    padding: 8px 14px;
    border-bottom: 1.5px solid var(--rule);
  }
  .contact-lines li:last-child { border-bottom: none; line-height: 1.3; }
  .contact-role {
    grid-column: 2; grid-row: 1 / span 2;
    display: grid; grid-template-rows: 1fr 1fr;
  }
  .role-title {
    font-size: 19px; font-weight: 400; letter-spacing: 2px;
    padding: 22px 14px 0;
    border-bottom: 1.5px solid var(--rule);
  }
  .role-phone {
    font-weight: 600; font-size: 20px; letter-spacing: .5px;
    line-height: 1.15;
    padding: 16px 14px 0;
  }
</style>
</head>
<body>
<main class="stage">
  <article class="card">
    <section class="card-face">
      <svg class="tree-art" viewBox="0 0 210 360" role="img" aria-label="Hand-textured golden pine tree illustration with exposed roots">
        <defs>
          <linearGradient id="treeTone" x1="0" y1="0" x2="0" y2="1">
            <stop offset="0" stop-color="var(--tree-gold)"/>
            <stop offset="1" stop-color="var(--tree-amber)"/>
          </linearGradient>
        </defs>
        <rect width="210" height="360" rx="40" fill="url(#treeTone)"/>
      </svg>
      <div class="brand">
        <div class="brand-line">
          <span class="brand-square"></span>
          <span class="brand-name">NORVANE</span>
        </div>
        <span class="brand-tagline">WOOD ARTISAN</span>
      </div>
    </section>
    <section class="contact-panel">
      <h1 class="contact-name">LUC NORVANE</h1>
      <ul class="contact-lines">
        <li>WWW.NORVANEWOOD.COM</li>
        <li>INFO@NORVANEWOOD.COM</li>
        <li>14 CEDAR LANE, HALTON, ON, L7K2B3<br>CANADA</li>
      </ul>
      <div class="contact-role">
        <p class="role-title">WOOD ARTISAN</p>
        <p class="role-phone">(031)<br>482 17 306 55</p>
      </div>
    </section>
  </article>
</main>
</body>
</html>
```